Infographic to communicate Cyber Security and Insurance Product Offering for IT Service Providers

We need an inspirational infographic that shows how TrellaWorks works with QDR (an MSP partner) to help organisations close the loop on cyber risk. The design should illustrate the layers of the IT infrastructure stack and the systems and processes that wrap around it to protect and mitigate against risk.
At the core: MSP Services (Desktop, Software, Website). Surrounding this: TrellaWorks Governance & Protection, leading into an Incident layer that connects to TrellaWorks Insurance and Incident Response, linked by a continuous feedback loop. The outer circle should represent the constant threat of cyber attack.
TrellaWorks core offerings for this graphic:
Plinth Verify (compliance/assurance product)
Plinth Cover
QDR Primary Services (directly connected to TrellaWorks):
Managed IT Services
Disaster Recovery as a Service (DRaaS)
E8 Security Packages
Cloud Hosting & Infrastructure
QDR Secondary Services (supporting but not directly anchored):
Telephony & Unified Communications
Networking Services
Data Backup & Storage Solutions
Professional Services & Consulting
Procurement & Licensing
Training & User Awareness
Style: Modern, professional, and client-friendly, with a technology-inspired colour palette.
Deliverables: Polished colour version plus editable source files — preferably in Figma, or alternatively if not possible using either Adobe Illustrator (.AI) or a layered Photoshop (.PSD) (e.g. industry standards for editable design).
Rewards: The winning design prize will be increased by $100, and we will also award $50 each to the 2nd and 3rd place runner-ups, as our way of giving a little more back.
A simple wireframe visual guide has been uploaded as a reference, but this should in no way limit or restrict your creativity. We encourage original, innovative approaches to bring this concept to life.
Ownership & Exclusivity: As per ArtMarquee’s T&Cs, all rights to the winning design will transfer to us once the project is complete for our ongoing use. We also kindly ask that the work created here remain exclusive to this project, meaning it won’t be reused or lightly modified for other clients in the future. The reason is simple: once we’ve invested in and paid for a design, we want to be confident it won’t turn up on a competitor’s website with just a different colour scheme. Thanks again for respecting that. [Note:- The designs submitted so far haven’t quite hit the mark, so I’ve put together a couple of slides to clarify direction. These outline the key stakeholders, the current IT services and challenges, how the Morvane product addresses those challenges, and a simple version of what we’d like the infographic to convey. Please review these slides carefully, as they should give you a clearer understanding of the story we want the design to tell.]
Target Market(s)
Small to Medium sized businesses
Colors
Designer to choose colors to be used in the design.
Look and feel

```html
<!DOCTYPE html>
<html lang="en">
<head>
<meta charset="utf-8">
<title>TrellaWorks – Closing the Loop on Cyber Risk</title>
<link rel="stylesheet" href="https://fonts.googleapis.com/css2?family=Montserrat:wght@500;600;700;800&display=swap">
<style>
  :root {
    --attack-red: #ec1c24;
    --brand-blue: #2a6cb6;
    --sky-blue: #6aaee0;
    --pale-blue: #c7def3;
    --mist-blue: #d9e9f8;
    --navy: #0b1550;
    --deep-navy: #1a3566;
    --ink: #1e1e1e;
    --paper: #ffffff;
  }
  html, body {
    margin: 0;
    padding: 0;
    width: 1043px;
    height: 1200px;
    overflow: hidden;
    background: var(--paper);
  }
  .poster {
    position: relative;
    width: 1043px;
    height: 1200px;
    background: var(--paper);
    font-family: "Montserrat", Arial, sans-serif;
  }
  .risk-loop {
    position: absolute;
    left: 101px;
    top: 68px;
    width: 840px;
    height: 840px;
  }
  .ring-label {
    font-weight: 600;
    fill: var(--paper);
    font-size: 26px;
    letter-spacing: 4px;
  }
  .band-label {
    font-weight: 700;
    fill: var(--paper);
    font-size: 23px;
    letter-spacing: 3px;
  }
  .inner-label {
    font-weight: 700;
    fill: var(--brand-blue);
    font-size: 20px;
    letter-spacing: 1.5px;
  }
  .feedback-label {
    font-weight: 600;
    font-size: 13px;
    letter-spacing: 1.5px;
  }
  .core-eyebrow {
    font-weight: 800;
    fill: var(--brand-blue);
    font-size: 44px;
  }
  .core-title {
    font-weight: 800;
    fill: var(--ink);
    font-size: 56px;
  }
  .service-tile rect {
    fill: var(--navy);
    stroke: var(--brand-blue);
    stroke-width: 3;
  }
  .service-tile text {
    font-weight: 800;
    fill: var(--paper);
    font-size: 36px;
  }
  .headline {
    position: absolute;
    left: 0;
    right: 0;
    top: 930px;
    margin: 0;
    text-align: center;
    color: var(--brand-blue);
    font-weight: 800;
    font-size: 86px;
    line-height: 100px;
    letter-spacing: -1px;
  }
  .tagline {
    position: absolute;
    left: 0;
    right: 0;
    top: 1042px;
    margin: 0;
    text-align: center;
    color: var(--ink);
    font-weight: 700;
    font-size: 46px;
    line-height: 46px;
    letter-spacing: -0.5px;
  }
</style>
</head>
<body>
<main class="poster">
  <svg class="risk-loop" viewBox="-600 -600 1200 1200" role="img" aria-label="Cyber risk loop: QDR MSP services at the core, wrapped by governance, protection, insurance, incident response and feedback, surrounded by cyber attack">
    <defs>
      <path id="attack-top" d="M -507 0 A 507 507 0 1 1 507 0 A 507 507 0 1 1 -507 0"/>
      <path id="attack-bottom" d="M -540 0 A 540 540 0 1 0 540 0 A 540 540 0 1 0 -540 0"/>
      <path id="feedback-path" d="M 0 432 A 432 432 0 1 1 0 -432 A 432 432 0 1 1 0 432"/>
      <path id="band-path" d="M -356 0 A 356 356 0 1 0 356 0 A 356 356 0 1 0 -356 0"/>
      <path id="governance-path" d="M 0 222 A 222 222 0 1 1 0 -222 A 222 222 0 1 1 0 222"/>
      <path id="protection-path" d="M 0 238 A 238 238 0 1 1 0 -238 A 238 238 0 1 1 0 238"/>
      <linearGradient id="band-shade" gradientUnits="userSpaceOnUse" x1="0" y1="-393" x2="0" y2="-190">
        <stop offset="0" stop-color="#78b6e8"/>
        <stop offset="1" stop-color="#2a6cb6"/>
      </linearGradient>
      <marker id="tip-sky" viewBox="0 0 10 10" refX="2" refY="5" markerWidth="3" markerHeight="3" orient="auto">
        <path d="M0 0 L10 5 L0 10 Z" fill="#6aaee0"/>
      </marker>
      <marker id="tip-blue" viewBox="0 0 10 10" refX="2" refY="5" markerWidth="3" markerHeight="3" orient="auto">
        <path d="M0 0 L10 5 L0 10 Z" fill="#2a6cb6"/>
      </marker>
      <marker id="tip-navy" viewBox="0 0 10 10" refX="2" refY="5" markerWidth="3" markerHeight="3" orient="auto">
        <path d="M0 0 L10 5 L0 10 Z" fill="#1a3566"/>
      </marker>
      <marker id="tip-pale" viewBox="0 0 10 10" refX="2" refY="5" markerWidth="3" markerHeight="3" orient="auto">
        <path d="M0 0 L10 5 L0 10 Z" fill="#c7def3"/>
      </marker>
    </defs>

    <!-- threat ring -->
    <circle class="attack-ring" r="532.5" fill="none" stroke="var(--attack-red)" stroke-width="121"/>
    <text class="ring-label"><textPath href="#attack-top" startOffset="25%" text-anchor="middle">CYBER ATTACK</textPath></text>
    <text class="ring-label"><textPath href="#attack-bottom" startOffset="25%" text-anchor="middle">CYBER ATTACK</textPath></text>

    <!-- feedback loop -->
    <g class="feedback-loop" fill="none" stroke-width="9">
      <path d="M -419 -29.3 A 420 420 0 0 1 7.3 -419.9" stroke="var(--sky-blue)" marker-end="url(#tip-sky)"/>
      <path d="M 22 -419.4 A 420 420 0 0 1 419.9 7.3" stroke="var(--brand-blue)" marker-end="url(#tip-blue)"/>
      <path d="M 419.4 22 A 420 420 0 0 1 -7.3 419.9" stroke="var(--deep-navy)" marker-end="url(#tip-navy)"/>
      <path d="M -22 419.4 A 420 420 0 0 1 -419.9 7.3" stroke="var(--pale-blue)" marker-end="url(#tip-pale)"/>
    </g>
    <text class="feedback-label" fill="var(--sky-blue)"><textPath href="#feedback-path" startOffset="38%" text-anchor="middle">FEEDBACK</textPath></text>
    <text class="feedback-label" fill="var(--brand-blue)"><textPath href="#feedback-path" startOffset="62.8%" text-anchor="middle">FEEDBACK</textPath></text>
    <text class="feedback-label" fill="var(--deep-navy)"><textPath href="#feedback-path" startOffset="86.9%" text-anchor="middle">FEEDBACK</textPath></text>
    <text class="feedback-label" fill="var(--pale-blue)"><textPath href="#feedback-path" startOffset="13.5%" text-anchor="middle">FEEDBACK</textPath></text>

    <!-- insurance & response band -->
    <circle class="response-band" r="344" fill="none" stroke="url(#band-shade)" stroke-width="98"/>
    <path class="incident-notch" d="M -32 292 L 32 292 L 0 324 Z" fill="var(--paper)"/>
    <text class="band-label"><textPath href="#band-path" startOffset="1.5%">INCIDENT RESPONSE</textPath></text>
    <text class="band-label"><textPath href="#band-path" startOffset="25%" text-anchor="middle">INCIDENT</textPath></text>
    <text class="band-label"><textPath href="#band-path" startOffset="33.2%">TRELLAWORKS INSURANCE</textPath></text>
    <g class="incident-arrows" stroke="var(--paper)" stroke-width="2.5" fill="var(--paper)">
      <line x1="-92" y1="337" x2="-138" y2="324"/>
      <path d="M -146 322 L -134 318 L -136 330 Z" stroke="none"/>
      <line x1="97" y1="337" x2="143" y2="324"/>
      <path d="M 151 322 L 139 318 L 141 330 Z" stroke="none"/>
    </g>

    <!-- governance & protection ring -->
    <g class="guard-arcs" fill="none" stroke="var(--mist-blue)" stroke-width="7">
      <path d="M -148.2 -219.7 A 265 265 0 0 1 234 -124.4"/>
      <path d="M 236.9 118.7 A 265 265 0 0 1 -158.4 212.5"/>
    </g>
    <text class="inner-label"><textPath href="#governance-path" startOffset="12%">TRELLAWORKS GOVERNANCE</textPath></text>
    <text class="inner-label"><textPath href="#protection-path" startOffset="75%" text-anchor="middle">PROTECTION</textPath></text>

    <!-- core services -->
    <text class="core-eyebrow" x="0" y="-130" text-anchor="middle">QDR MSP</text>
    <text class="core-title" x="0" y="-78" text-anchor="middle">SERVICES</text>
    <g class="service-tile">
      <rect x="-150" y="-40" width="300" height="60" rx="9"/>
      <text x="0" y="3" text-anchor="middle" dominant-baseline="middle">DESKTOP</text>
    </g>
    <g class="service-tile">
      <rect x="-150" y="28" width="300" height="60" rx="9"/>
      <text x="0" y="71" text-anchor="middle" dominant-baseline="middle">SOFTWARE</text>
    </g>
    <g class="service-tile">
      <rect x="-150" y="96" width="300" height="60" rx="9"/>
      <text x="0" y="139" text-anchor="middle" dominant-baseline="middle">WEBSITE</text>
    </g>
  </svg>

  <h1 class="headline">TRELLAWORKS</h1>
  <p class="tagline">CLOSING THE LOOP ON<br>CYBER RISK</p>
</main>
</body>
</html>
```